Bref créative
Stationary for Ministry
R L Brandt Harvest Ministries
Use same font as used in my logo
Can modify at designer's discretion
Professional
R L Brandt
Founder
418 W. Corvell Blvd
Longview, TX 75612
rlbtx7@mailvane.net
rlbrandt.com
just put the logo on the front
all contact info on back
Hello! This file should be in a transparent format so no lines or shadows show up.

```html
<!DOCTYPE html>
<html lang="en">
<head>
<meta charset="utf-8">
<title>R L Brandt Harvest Ministries — Stationery Set</title>
<link href="https://fonts.googleapis.com/css2?family=Open+Sans:wght@400;600;700&display=swap" rel="stylesheet">
<style>
:root{
  --bg:#000;
  --paper:#fff;
  --blue:#1a6fc4;
  --blue-dark:#0b4d9b;
  --green:#8cc63f;
  --orange:#f7941d;
  --gold:#e2a62a;
  --ink:#555;
  --rule:#d6d6d6;
  --tree:#dfe9c9;
}
*{box-sizing:border-box;margin:0;padding:0}
html,body{width:1200px;height:898px;overflow:hidden;background:var(--bg)}
body{position:relative;font-family:"Open Sans",Arial,sans-serif;color:var(--ink)}
.piece{position:absolute;background:var(--paper);overflow:hidden}
/* footer band: plain stacked stripes */
.band{position:absolute;left:0;bottom:0;width:100%;display:flex;flex-direction:column}
.band .g{height:4px;background:var(--green)}
.band .o{height:3px;background:var(--orange)}
.band .b{flex:1;background:linear-gradient(var(--blue),var(--blue-dark))}
.band.top{top:0;bottom:auto;flex-direction:column-reverse}
.brand{display:flex;align-items:center;gap:4px;color:var(--blue);font-weight:700;line-height:1;white-space:nowrap}
.brand .dot{width:1em;height:1em;border-radius:50%;background:var(--green);flex:none}
.brand .sub{display:block;font-size:.38em;font-weight:700;letter-spacing:.5px;color:var(--blue);margin-top:1px}
.contact{position:absolute;font-size:5px;line-height:1.5;color:var(--ink);border-left:1px solid var(--green);padding-left:4px;white-space:nowrap}
.tree{position:absolute;border-radius:50% 50% 40% 40%;background:radial-gradient(circle at 50% 40%,var(--tree),rgba(223,233,201,0) 70%)}
.lines{position:absolute;left:18px;right:18px}
.lines i{display:block;height:2.4px;background:var(--rule);margin-bottom:4px;border-radius:1px}
.form-grid{position:absolute;left:18px;right:18px;top:88px;font-size:6px;display:grid;grid-template-columns:1fr 1fr;column-gap:14px;row-gap:6px}
.form-grid span{border-bottom:1px solid var(--rule);padding-bottom:2px}
.form-bar{position:absolute;left:18px;right:18px;top:160px;height:12px;background:var(--green);display:flex;justify-content:space-around;align-items:center;font-size:5px;color:#fff}
.form-head{position:absolute;left:18px;top:180px;font-size:6.5px;font-weight:700;color:var(--blue)}
.letter{position:absolute;left:18px;right:22px;top:62px;font-size:4.6px;line-height:1.55}
.letter p{margin-bottom:5px}
.inv-title{position:absolute;left:18px;top:60px;font-size:11px;font-weight:700;color:var(--green)}
.inv-table{position:absolute;left:18px;right:18px;top:110px;border:1px solid var(--rule);font-size:5px}
.inv-table .row{display:grid;grid-template-columns:3fr 1fr 1fr 1fr;height:11px;border-bottom:1px solid #eee;align-items:center;padding:0 3px}
.inv-table .head{background:var(--green);color:#fff;font-weight:600}
.inv-foot{position:absolute;left:0;right:0;bottom:0;height:22px;background:var(--blue-dark);color:#fff;font-size:6px;text-align:center;line-height:22px}
.compliments{position:absolute;left:0;right:0;bottom:0;height:20px;background:var(--blue);color:#fff;font-size:8px;padding-left:14px;line-height:20px}
.cd{border-radius:50%}
.cd .hole{position:absolute;left:50%;top:50%;width:26px;height:26px;margin:-13px 0 0 -13px;border-radius:50%;background:var(--bg);box-shadow:0 0 0 8px #e8e8e8}
</style>
</head>
<body>

<!-- Fax / form sheet -->
<section class="piece" style="left:17px;top:12px;width:280px;height:377px">
  <div class="brand" style="position:absolute;left:18px;top:14px;font-size:15px"><span class="dot"></span><span>R L BRANDT<span class="sub">HARVEST MINISTRIES</span></span></div>
  <div class="contact" style="left:200px;top:14px">418 W. Corvell Blvd<br>Longview, TX 75612<br>rlbtx7@mailvane.net<br>rlbrandt.com</div>
  <div class="form-grid"><span>To:</span><span>From:</span><span>Fax:</span><span>Pages:</span><span>Phone:</span><span>Date:</span><span>Re:</span><span>CC:</span></div>
  <div class="form-bar"><span>Urgent</span><span>For Review</span><span>Please Reply</span><span>Please Comment</span></div>
  <div class="form-head">COMMENTS:</div>
  <div class="tree" role="img" aria-label="Faint tree illustration" style="right:14px;bottom:50px;width:90px;height:110px"></div>
  <div class="band" style="height:44px"><i class="g"></i><i class="o"></i><i class="b"></i></div>
</section>

<!-- Letterhead -->
<section class="piece" style="left:312px;top:12px;width:280px;height:377px">
  <div class="brand" style="position:absolute;left:18px;top:14px;font-size:15px"><span class="dot"></span><span>R L BRANDT<span class="sub">HARVEST MINISTRIES</span></span></div>
  <div class="contact" style="left:200px;top:14px">418 W. Corvell Blvd<br>Longview, TX 75612<br>rlbtx7@mailvane.net<br>rlbrandt.com</div>
  <div class="letter">
    <p>Mr. John Sample<br>120 Oak Street<br>Tyler, TX 75701</p>
    <p>Dear Friends and Partners,</p>
    <p>Thank you for standing with our ministry this season. Your prayers and gifts help us reach families across East Texas with hope, music and the good news.</p>
    <p>This year we will hold four harvest gatherings, serve local churches and train new leaders. Every event is open to the whole community.</p>
    <p>We are grateful for your faithful support and look forward to sharing more stories with you soon.</p>
    <p>Blessings,<br><br>R L Brandt<br>Founder</p>
  </div>
  <div class="tree" role="img" aria-label="Faint tree illustration" style="right:14px;bottom:50px;width:90px;height:110px"></div>
  <div class="band" style="height:44px"><i class="g"></i><i class="o"></i><i class="b"></i></div>
</section>

<!-- Invoice -->
<section class="piece" style="left:606px;top:12px;width:280px;height:377px">
  <div class="brand" style="position:absolute;left:18px;top:14px;font-size:15px"><span class="dot"></span><span>R L BRANDT<span class="sub">HARVEST MINISTRIES</span></span></div>
  <div class="contact" style="left:200px;top:14px">418 W. Corvell Blvd<br>Longview, TX 75612<br>rlbtx7@mailvane.net<br>rlbrandt.com</div>
  <div class="inv-title">INVOICE</div>
  <div style="position:absolute;left:18px;top:80px;font-size:5px;line-height:1.6">Date:<br>Invoice #<br>Bill To:</div>
  <div class="inv-table">
    <div class="row head"><span>Description</span><span>Qty</span><span>Price</span><span>Amount</span></div>
    <div class="row"></div><div class="row"></div><div class="row"></div><div class="row"></div><div class="row"></div><div class="row"></div><div class="row"></div><div class="row"></div><div class="row"></div><div class="row"></div><div class="row"></div><div class="row"></div>
  </div>
  <div class="band" style="height:46px"><i class="g"></i><i class="o"></i><i class="b"></i></div>
  <div class="inv-foot">Thank You For Your Business!</div>
</section>

<!-- Letterhead back -->
<section class="piece" style="left:900px;top:12px;width:283px;height:377px">
  <div class="band top" style="height:62px"><i class="g"></i><i class="o"></i><i class="b"></i></div>
  <div class="contact" style="left:14px;top:10px;color:#fff;border-color:#fff">418 W. Corvell Blvd<br>Longview, TX 75612<br>rlbtx7@mailvane.net<br>rlbrandt.com</div>
  <div class="brand" style="position:absolute;left:120px;top:132px;font-size:20px"><span class="dot"></span><span>R L BRANDT<span class="sub">HARVEST MINISTRIES</span></span></div>
  <div class="tree" role="img" aria-label="Faint tree illustration" style="left:100px;top:180px;width:100px;height:120px"></div>
  <div class="band" style="height:44px"><i class="g"></i><i class="o"></i><i class="b"></i></div>
</section>

<!-- Envelope with flaps -->
<section class="piece" style="left:17px;top:402px;width:307px;height:275px">
  <svg width="307" height="275" style="position:absolute;left:0;top:0">
    <defs><linearGradient id="blueFill" x1="0" y1="0" x2="0" y2="1"><stop offset="0" stop-color="#2a86d8"/><stop offset="1" stop-color="#0b4d9b"/></linearGradient></defs>
    <rect width="307" height="130" fill="url(#blueFill)"/>
    <path d="M0 0 L153 52 L307 0 Z" fill="#fff"/>
    <path d="M0 130 L307 130 L307 150 L153 215 L0 150Z" fill="#e2a62a"/>
    <path d="M0 150 L153 215 L307 150" fill="none" stroke="#f7c768" stroke-width="2"/>
    <circle cx="153" cy="28" r="9" fill="#1a6fc4"/>
    <circle cx="153" cy="172" r="9" fill="#fff"/>
  </svg>
  <div class="brand" style="position:absolute;left:16px;top:96px;font-size:11px;color:#fff"><span>R L BRANDT</span></div>
  <div class="brand" style="position:absolute;left:16px;top:228px;font-size:11px"><span class="dot"></span><span>R L BRANDT</span></div>
  <div style="position:absolute;left:40px;bottom:10px;font-size:5px">rlbrandt.com</div>
</section>

<!-- Compliment slips -->
<section class="piece" style="left:338px;top:402px;width:314px;height:129px">
  <div class="brand" style="position:absolute;left:14px;top:18px;font-size:14px"><span class="dot"></span><span>R L BRANDT<span class="sub">HARVEST MINISTRIES</span></span></div>
  <div class="contact" style="left:240px;top:14px">418 W. Corvell Blvd<br>Longview, TX 75612<br>rlbtx7@mailvane.net<br>rlbrandt.com</div>
  <div class="band" style="height:26px"><i class="g"></i><i class="o"></i><i class="b"></i></div>
</section>
<section class="piece" style="left:338px;top:540px;width:314px;height:129px">
  <div class="brand" style="position:absolute;left:14px;top:18px;font-size:14px"><span class="dot"></span><span>R L BRANDT<span class="sub">HARVEST MINISTRIES</span></span></div>
  <div class="contact" style="left:240px;top:14px">418 W. Corvell Blvd<br>Longview, TX 75612<br>rlbtx7@mailvane.net<br>rlbrandt.com</div>
  <div class="band" style="height:42px"><i class="g"></i><i class="o"></i><i class="b"></i></div>
  <div class="compliments">With Best Compliments</div>
</section>

<!-- Notepad -->
<section class="piece" style="left:664px;top:402px;width:202px;height:275px">
  <div class="lines" style="top:28px"><i></i><i></i><i></i><i></i><i></i><i></i><i></i><i></i><i></i><i></i><i></i><i></i><i></i><i></i><i></i><i></i><i></i><i></i><i></i><i></i><i></i><i></i><i></i><i></i><i></i><i></i><i></i><i></i><i></i><i></i><i></i><i></i></div>
  <div class="band" style="height:28px"><i class="g"></i><i class="o"></i><i class="b"></i></div>
</section>

<!-- Large envelope -->
<section class="piece" style="left:879px;top:402px;width:304px;height:275px">
  <svg width="304" height="60" style="position:absolute;left:0;top:0">
    <path d="M0 0 H304 V20 L152 58 L0 20Z" fill="#1a6fc4"/>
    <circle cx="152" cy="22" r="10" fill="#fff"/>
  </svg>
  <div class="brand" style="position:absolute;left:16px;top:78px;font-size:20px"><span class="dot"></span><span>R L BRANDT<span class="sub">HARVEST MINISTRIES</span></span></div>
  <div class="contact" style="left:222px;top:74px">418 W. Corvell Blvd<br>Longview, TX 75612<br>rlbtx7@mailvane.net<br>rlbrandt.com</div>
  <div class="tree" role="img" aria-label="Faint tree illustration" style="left:14px;top:130px;width:70px;height:90px"></div>
  <div class="band" style="height:36px"><i class="g"></i><i class="o"></i><i class="b"></i></div>
</section>

<!-- Folder -->
<section class="piece" style="left:29px;top:711px;width:166px;height:141px">
  <div class="brand" style="position:absolute;left:12px;top:38px;font-size:14px"><span class="dot"></span><span>R L BRANDT<span class="sub">HARVEST MINISTRIES</span></span></div>
  <div class="band" style="height:28px"><i class="g"></i><i class="o"></i><i class="b"></i></div>
</section>

<!-- CD -->
<section class="piece cd" style="left:209px;top:711px;width:122px;height:122px">
  <div class="brand" style="position:absolute;left:14px;top:22px;font-size:11px"><span>R L BRANDT</span></div>
  <div class="band" style="height:40px"><i class="g"></i><i class="o"></i><i class="b"></i></div>
  <div class="hole"></div>
</section>

<!-- Business cards -->
<section class="piece" style="left:433px;top:694px;width:156px;height:78px">
  <div class="brand" style="position:absolute;left:8px;top:14px;font-size:10px"><span class="dot"></span><span>R L BRANDT<span class="sub">HARVEST MINISTRIES</span></span></div>
  <div class="contact" style="left:98px;top:10px;font-size:4px">R L Brandt<br>Founder<br>418 W. Corvell Blvd<br>Longview, TX 75612<br>rlbtx7@mailvane.net</div>
  <div class="band" style="height:16px"><i class="g" style="height:2px"></i><i class="o" style="height:2px"></i><i class="b"></i></div>
</section>
<section class="piece" style="left:613px;top:694px;width:156px;height:78px;background:linear-gradient(#2a86d8,#0b4d9b)">
  <div class="brand" style="position:absolute;left:38px;top:28px;font-size:12px;color:#fff"><span class="dot" style="background:#fff"></span><span>R L BRANDT</span></div>
</section>
<section class="piece" style="left:523px;top:794px;width:156px;height:78px">
  <div class="brand" style="position:absolute;left:8px;top:12px;font-size:10px"><span class="dot"></span><span>R L BRANDT</span></div>
  <div style="position:absolute;left:100px;top:12px;font-size:4.5px;line-height:1.5">rlbrandt.com</div>
  <div class="band" style="height:26px"><i class="g" style="height:3px"></i><i class="o" style="height:2px"></i><i class="b"></i></div>
</section>

</body>
</html>
```